Fachgeschäft für Uhren & Schmuck benötigt Logo & Visitenkarte
Zielgruppe
Wir sind ein Fachgeschäft für Uhren & Schmuck
Aufgabenstellung
Es sollte ein gut lesbares Logo sein, verspielt modern.

```html
<!DOCTYPE html>
<html lang="de">
<head>
<meta charset="utf-8">
<title>Torvim Visitenkarte</title>
<link rel="stylesheet" href="https://fonts.googleapis.com/css2?family=EB+Garamond:wght@400;600&display=swap">
<style>
  :root {
    --paper: #ffffff;
    --ink: #14131c;
    --crop: #1a1a1a;
  }
  html, body {
    margin: 0;
    padding: 0;
    overflow: hidden;
    background: var(--paper);
  }
  .card {
    position: relative;
    width: 874px;
    height: 1200px;
    background: var(--paper);
    overflow: hidden;
    font-family: "EB Garamond", Garamond, serif;
    color: var(--ink);
  }
  .crop-marks {
    position: absolute;
    inset: 0;
  }
  .brand {
    position: absolute;
    top: 300px;
    left: 0;
    width: 874px;
    text-align: center;
  }
  .brand-name {
    margin: 0;
    font-family: "EB Garamond", Garamond, serif;
    font-weight: 400;
    font-size: 60px;
    line-height: 1;
    color: var(--ink);
  }
  .holder {
    position: absolute;
    top: 756px;
    left: 0;
    width: 874px;
    margin: 0;
    text-align: center;
    font-weight: 600;
    font-size: 29px;
  }
  .contact {
    position: absolute;
    top: 880px;
    left: 0;
    width: 874px;
    margin: 0;
    text-align: center;
    font-style: normal;
    font-size: 26px;
    line-height: 32px;
  }
  .contact span { display: block; }
  .contact .phone { letter-spacing: 0.06em; }
</style>
</head>
<body>
<div class="card">
  <svg class="crop-marks" width="874" height="1200" viewBox="0 0 874 1200" aria-hidden="true">
    <g stroke="var(--crop)" stroke-width="1.2">
      <line x1="138" y1="0" x2="138" y2="92"/>
      <line x1="736" y1="0" x2="736" y2="92"/>
      <line x1="0" y1="138" x2="92" y2="138"/>
      <line x1="782" y1="138" x2="874" y2="138"/>
      <line x1="0" y1="1061" x2="92" y2="1061"/>
      <line x1="782" y1="1061" x2="874" y2="1061"/>
      <line x1="138" y1="1108" x2="138" y2="1200"/>
      <line x1="736" y1="1108" x2="736" y2="1200"/>
    </g>
  </svg>

  <header class="brand">
    <h1 class="brand-name">Torvim</h1>
  </header>

  <p class="holder">Konrad Elsbeck</p>

  <address class="contact">
    <span>Lindenhof Allee 21</span>
    <span>20537 Hamburg</span>
    <span>elsbeck@torvim-uhren.de</span>
    <span class="phone">040-5512874419</span>
  </address>
</div>
</body>
</html>
```